Physical Therapy Center for children Business Card

We need a Business Card for our company (Physical Therapy for children and youth with special needs) in Lisbon, Portugal. The name of the company is "Ninho de Luz"

The card must contain the following info:
- Logo: see uploaded file
- Name: Ninho de Luz
- Slogan: Plantamos carinho, vemos crescer risos, celebramos conquistas!
- Service: Terapias Especializadas
- Address: Rua Henrique Lobato Farinha 9C
- ZipCode: 2741-318 Ribamar do Sal
- E-mail: geral@velado.pt
- Site: www.velado.pt
- Facebook: www.facebook.com/ninhodeluz
- Phone: +351 21 584 62 07
- Cell Phone: +351 96 731 84 25

The stationary should have contain all info from business card.

Target Market(s)

Parents of children with special needs

Industry/Entity Type

Physical Therapy

Contact Information for Business Card

The card design should be compatible with http://www.quellprensa.com/product2/order_detail.php?gid=40

Requirements
Should not have
• The business card should not have a Black background. Use white or other color.

```html
<!DOCTYPE html>
<html lang="pt">
<head>
<meta charset="utf-8">
<title>Ninho de Luz — Cartão de Visita</title>
<link rel="stylesheet" href="https://fonts.googleapis.com/css2?family=Source+Sans+3:wght@400;600;700&display=swap">
<style>
  :root {
    --teal: #23b4a2;
    --purple: #784370;
    --red: #e8463c;
    --slogan: #8b817b;
    --white: #ffffff;
    --stage: #4a4a4a;
  }
  * { margin: 0; padding: 0; box-sizing: border-box; }
  html, body { width: 1200px; height: 1200px; overflow: hidden; }
  body {
    background: var(--stage);
    font-family: "Source Sans 3", "Myriad Pro", Arial, sans-serif;
    position: relative;
  }
  .card {
    position: absolute;
    width: 796px;
    height: 452px;
    background: var(--white);
    overflow: hidden;
  }
  .card--front { left: 202px; top: 110px; }
  .card--back { left: 204px; top: 638px; }
  .card__shapes { position: absolute; inset: 0; }

  .brand-mark {
    position: absolute;
    left: 46px;
    top: 46px;
    width: 170px;
    height: 170px;
    display: flex;
    align-items: center;
    justify-content: center;
  }
  .brand-mark__dot {
    width: 120px; height: 120px; border-radius: 50%;
    background: var(--teal);
  }
  .brand-name {
    position: absolute;
    left: 68px;
    top: 276px;
    font-size: 33px;
    font-weight: 400;
    color: var(--red);
    line-height: 1;
    white-space: nowrap;
  }
  .slogan {
    position: absolute;
    left: 68px;
    top: 322px;
    font-size: 20px;
    line-height: 26.7px;
    color: var(--slogan);
    white-space: nowrap;
  }

  .person {
    position: absolute;
    right: 38px;
    top: 88px;
    text-align: right;
    color: var(--white);
  }
  .person__name { font-size: 31px; font-weight: 700; line-height: 1.1; }
  .person__role { font-size: 21px; font-weight: 400; line-height: 1.3; }

  .contacts {
    position: absolute;
    right: 38px;
    top: 183px;
    list-style: none;
    color: var(--white);
    font-size: 21px;
  }
  .contacts li {
    display: flex;
    justify-content: flex-end;
    align-items: center;
    height: 26.7px;
    white-space: nowrap;
  }
  .contacts svg { width: 22px; height: 20px; margin-left: 12px; flex: none; }

  .address {
    position: absolute;
    right: 38px;
    top: 345px;
    text-align: right;
    color: var(--white);
    font-size: 21px;
    line-height: 27px;
    white-space: nowrap;
  }

  .back-brand {
    position: absolute;
    inset: 0;
    display: flex;
    align-items: center;
    justify-content: center;
    gap: 18px;
  }
  .back-brand__dot { width: 80px; height: 80px; border-radius: 50%; background: var(--teal); }
  .back-brand__name { font-size: 40px; font-weight: 600; color: var(--teal); }
</style>
</head>
<body>

<section class="card card--front">
  <svg class="card__shapes" viewBox="0 0 796 452" width="796" height="452" aria-hidden="true">
    <polygon points="173,0 796,0 796,452 461,452" fill="var(--teal)"/>
    <polygon points="358,290 256,452 461,452" fill="var(--purple)"/>
  </svg>

  <div class="brand-mark"><span class="brand-mark__dot"></span></div>
  <p class="brand-name">Ninho de Luz</p>
  <p class="slogan">Plantamos carinho,<br>vemos crescer risos,<br>celebramos conquistas!</p>

  <div class="person">
    <p class="person__name">Marta Sequeira</p>
    <p class="person__role">Managing Partner</p>
  </div>

  <ul class="contacts">
    <li>+351 21 584 62 07
      <svg viewBox="0 0 22 20"><path d="M2 8 Q11 0 20 8 L17 10 L15 7 Q11 5 7 7 L5 10 Z" fill="#fff"/><path d="M5 11 L7 8 H15 L17 11 V17 H5 Z" fill="#fff"/><circle cx="11" cy="13" r="2.4" fill="var(--teal)"/></svg>
    </li>
    <li>+351 96 731 84 25
      <svg viewBox="0 0 22 20"><rect x="6" y="1" width="10" height="18" rx="2" fill="none" stroke="#fff" stroke-width="2"/><line x1="9" y1="16" x2="13" y2="16" stroke="#fff" stroke-width="1.5"/></svg>
    </li>
    <li>geral@velado.pt
      <svg viewBox="0 0 22 20"><rect x="1" y="4" width="20" height="13" fill="#fff"/><path d="M1 4 L11 12 L21 4 M1 17 L8 10 M21 17 L14 10" fill="none" stroke="var(--teal)" stroke-width="1.5"/></svg>
    </li>
    <li>www.velado.pt
      <svg viewBox="0 0 22 20"><g fill="none" stroke="#fff" stroke-width="1.5"><circle cx="11" cy="10" r="8.5"/><ellipse cx="11" cy="10" rx="4" ry="8.5"/><line x1="2.5" y1="10" x2="19.5" y2="10"/><line x1="11" y1="1.5" x2="11" y2="18.5"/><path d="M4 5.5 H18 M4 14.5 H18"/></g></svg>
    </li>
    <li>www.rederoda.com/ninhodeluz
      <svg viewBox="0 0 22 20"><rect x="2" y="0" width="19" height="20" fill="#fff"/></svg>
    </li>
  </ul>

  <p class="address">Rua Henrique Lobato Farinha 9C<br>2741-318 Ribamar do Sal</p>
</section>

<section class="card card--back">
  <div class="back-brand">
    <span class="back-brand__dot"></span>
    <span class="back-brand__name">Ninho de Luz</span>
  </div>
</section>

</body>
</html>
```